Summit Enrolla needs a 8.5" X 11" flyer to give to college presidents

We need a flyer design for Summit Enrolla that briefly explains what we do and encourages college presidents to give the flyer to their directors of admission. Please be consistent with our brand www.summitenrolla.example. I've attached an example of a cool three dimensional flyer that I like...but I'm open to all ideas.

FRONT: The first on-line and fully automated recruiting tool that allows admissions officers to electronically contact high school seniors and send them invitations to apply that include estimates of merit aid.

BACK: Summit Enrolla brings your college or university students' mobile devices and desktops. Knowing their credentials, admissions offers can send either a single student or groups of students invitations to apply that include offers of merit aid. Your school’s invitation is a recruiting document that appeals to students and parents with a clear price signal, and to students and counselors with customizable links to your college or universities website, rankings, social media and any particular information or commendation.

For information about how Summit Enrolla fits into your enrollment strategy and expands your access to students, families and counselors, please contact us by phone 866.512.2740 or email admin@summitenrolla.example. An on-line presentation of Summit Enrolla takes less than 30 minutes.

Target Market(s)

college presidents and admissions officers

Industry/Entity Type

Education

Requirements
Must have
• front and back designs
Nice to have
• a look of depth or three dimensions

```html
<!DOCTYPE html>
<html lang="en">
<head>
<meta charset="utf-8">
<title>Summit Enrolla – Flyer Front and Back</title>
<link rel="stylesheet" href="https://fonts.googleapis.com/css2?family=Arvo:wght@700&family=Cinzel:wght@600&family=Libre+Baskerville&family=Open+Sans:wght@400&display=swap">
<style>
  :root {
    --canvas-bg: #e6e7e8;
    --navy: #1d3a5c;
    --red-light: #a3222a;
    --red-dark: #5e0f14;
    --contact-red: #8e1b22;
    --panel-light: #dcdddf;
    --panel-mid: #b3b6b9;
    --steel: #8d9297;
    --steel-dark: #5f6469;
    --charcoal: #262728;
    --white: #ffffff;
    --footer-text: #c9cacb;
  }
  * { margin: 0; padding: 0; box-sizing: border-box; }
  html, body { width: 1200px; height: 800px; overflow: hidden; }
  body {
    background: var(--canvas-bg);
    display: flex;
    align-items: center;
    justify-content: center;
    gap: 60px;
  }
  .flyer {
    position: relative;
    width: 540px;
    height: 699px;
    overflow: hidden;
    box-shadow: 0 6px 18px rgba(0,0,0,.25);
  }
  .flyer-art { position: absolute; inset: 0; }

  /* FRONT */
  .front-brand {
    position: absolute;
    top: 110px; left: 0; right: 0;
    display: flex; align-items: center; justify-content: center; gap: 14px;
    font-family: "Arvo", Georgia, serif;
    font-weight: 700;
    font-size: 44px;
    color: var(--navy);
  }
  .brand-mark { width: 18px; height: 18px; background: var(--navy); }
  .front-statement {
    position: absolute;
    top: 230px; left: 100px; right: 100px;
    font-family: "Arvo", Georgia, serif;
    font-weight: 700;
    font-size: 23px;
    line-height: 1.72;
    text-align: center;
    color: var(--navy);
  }

  /* BACK */
  .back-body {
    position: absolute;
    top: 68px; left: 92px; right: 28px;
    font-family: "Open Sans", Arial, sans-serif;
    font-size: 15.5px;
    line-height: 1.5;
    text-align: justify;
    color: var(--white);
  }
  .back-callout {
    position: absolute;
    top: 330px; left: 96px; right: 30px;
    padding: 14px 18px 16px;
    background: linear-gradient(180deg, #e4e5e6, #b9bbbd);
    border-radius: 10px;
    font-family: "Arvo", Georgia, serif;
    font-weight: 700;
    font-size: 17px;
    line-height: 1.2;
    text-align: justify;
    text-align-last: left;
    color: var(--navy);
  }
  .back-callout .lead { display: block; text-align: center; }
  .contact-heading {
    position: absolute;
    top: 520px; left: 70px; right: 0;
    text-align: center;
    font-family: "Cinzel", Georgia, serif;
    font-weight: 600;
    font-size: 24px;
    color: var(--contact-red);
  }
  .contact-row {
    position: absolute;
    top: 568px; left: 92px; right: 20px;
    display: flex; align-items: center; gap: 22px;
    font-family: "Libre Baskerville", Georgia, serif;
    font-size: 14px;
    color: var(--charcoal);
  }
  .contact-item { display: flex; align-items: center; gap: 8px; }
  .contact-icon { width: 22px; height: 22px; flex: none; }
  .back-footer {
    position: absolute;
    top: 630px; left: 70px; right: 0;
    text-align: center;
    font-family: "Libre Baskerville", Georgia, serif;
    font-size: 12px;
    line-height: 1.45;
    color: var(--footer-text);
  }
</style>
</head>
<body>

<section class="flyer flyer-front" aria-label="Flyer front">
  <svg class="flyer-art" viewBox="0 0 540 699" preserveAspectRatio="none" aria-hidden="true">
    <defs>
      <linearGradient id="frontBase" x1="0" y1="0" x2="1" y2="0">
        <stop offset="0" stop-color="#6e7378"/>
        <stop offset=".5" stop-color="#a5aaae"/>
        <stop offset="1" stop-color="#6e7378"/>
      </linearGradient>
      <linearGradient id="frontPanel" x1="0" y1="0" x2="0" y2="1">
        <stop offset="0" stop-color="#e2e3e4"/>
        <stop offset="1" stop-color="#a9acaf"/>
      </linearGradient>
      <linearGradient id="bevelLeft" x1="0" y1="0" x2="1" y2="0">
        <stop offset="0" stop-color="#7c8186"/>
        <stop offset="1" stop-color="#c9cbcd"/>
      </linearGradient>
      <linearGradient id="bevelRight" x1="0" y1="0" x2="1" y2="0">
        <stop offset="0" stop-color="#c9cbcd"/>
        <stop offset="1" stop-color="#6f7479"/>
      </linearGradient>
      <linearGradient id="frontFloor" x1="0" y1="0" x2="0" y2="1">
        <stop offset="0" stop-color="#3a3b3d"/>
        <stop offset="1" stop-color="#1c1d1e"/>
      </linearGradient>
    </defs>
    <rect width="540" height="699" fill="url(#frontBase)"/>
    <rect x="0" y="0" width="22" height="699" fill="#585d62"/>
    <rect x="518" y="0" width="22" height="699" fill="#585d62"/>
    <rect x="0" y="570" width="540" height="129" fill="url(#frontFloor)"/>
    <polygon points="40,40 92,80 92,620 40,660" fill="url(#bevelLeft)"/>
    <polygon points="500,40 448,80 448,620 500,660" fill="url(#bevelRight)"/>
    <polygon points="40,40 500,40 448,80 92,80" fill="#eeeff0"/>
    <rect x="92" y="80" width="356" height="540" fill="url(#frontPanel)"/>
    <polygon points="92,620 448,620 500,660 40,660" fill="#55595d"/>
  </svg>
  <div class="front-brand"><span class="brand-mark"></span>Summit Enrolla</div>
  <p class="front-statement">The first on-line and fully automated recruiting tool that allows admissions officers to electronically contact high school seniors and send them invitations to apply that include estimates of merit aid.</p>
</section>

<section class="flyer flyer-back" aria-label="Flyer back">
  <svg class="flyer-art" viewBox="0 0 540 699" preserveAspectRatio="none" aria-hidden="true">
    <defs>
      <radialGradient id="redPanel" cx=".55" cy=".45" r=".75">
        <stop offset="0" stop-color="#a3222a"/>
        <stop offset="1" stop-color="#5e0f14"/>
      </radialGradient>
      <linearGradient id="sideStrip" x1="0" y1="0" x2="1" y2="0">
        <stop offset="0" stop-color="#5f6469"/>
        <stop offset="1" stop-color="#c3c6c8"/>
      </linearGradient>
      <linearGradient id="contactBand" x1="0" y1="0" x2="0" y2="1">
        <stop offset="0" stop-color="#e6e7e8"/>
        <stop offset="1" stop-color="#c2c4c6"/>
      </linearGradient>
      <linearGradient id="backFloor" x1="0" y1="0" x2="0" y2="1">
        <stop offset="0" stop-color="#4a4c4e"/>
        <stop offset="1" stop-color="#1e1f20"/>
      </linearGradient>
    </defs>
    <rect width="540" height="699" fill="url(#backFloor)"/>
    <rect x="0" y="0" width="540" height="48" fill="#2f3031"/>
    <rect x="70" y="48" width="470" height="460" fill="url(#redPanel)"/>
    <rect x="70" y="508" width="470" height="110" fill="url(#contactBand)"/>
    <polygon points="0,0 40,0 70,48 70,618 40,640 0,640" fill="url(#sideStrip)"/>
    <polygon points="40,0 70,0 70,48" fill="#3b3d3f"/>
  </svg>
  <p class="back-body">Summit Enrolla brings your college or university students’ mobile devices and desktops. Knowing their credentials, admissions offers can send either a single student or groups of students invitations to apply that include offers of merit aid. Your school’s invitation is a recruiting document that appeals to students and parents with a clear price signal, and to students and counselors with customizable links to your college or universities website, rankings, social media and any particular information or commendation.</p>
  <p class="back-callout"><span class="lead">For information about how</span>Summit Enrolla fits into your enrollment strategy and expands your access to students, families and counselors, please</p>
  <h2 class="contact-heading">Contact us by</h2>
  <div class="contact-row">
    <span class="contact-item">
      <svg class="contact-icon" viewBox="0 0 22 22" aria-hidden="true"><circle cx="11" cy="11" r="10" fill="#fff" stroke="#888" stroke-width="1"/><rect x="7.5" y="5" width="7" height="12" rx="1.5" fill="none" stroke="#262728" stroke-width="1.6"/><circle cx="11" cy="14.5" r=".9" fill="#262728"/></svg>
      866.512.2740
    </span>
    <span class="contact-item">
      <svg class="contact-icon" viewBox="0 0 22 22" aria-hidden="true"><circle cx="11" cy="11" r="10" fill="#fff" stroke="#888" stroke-width="1"/><rect x="5.5" y="7" width="11" height="8" fill="none" stroke="#262728" stroke-width="1.4"/><path d="M5.5 7 L11 11.5 L16.5 7" fill="none" stroke="#262728" stroke-width="1.4"/></svg>
      admin@summitenrolla.example
    </span>
  </div>
  <p class="back-footer">An on-line presentation of Summit Enrolla<br>takes less than 30 minutes.</p>
</section>

</body>
</html>
```